Attractive door board for entrance beautysalon

Make an attractive design for a board that can be glued on the front door of a beauty salon. The salon location has no window in the front so I need something catchy and attractive. The door board contains a list of the services and the website: www.velmora.be, and the text "Enkel op afspraak, bel 0486319542"

Target Market(s)

woman between 16 and 99 years old

Industry/Entity Type

Beauty Salon

Font styles to use
Sans Serif

Requirements
Must have
• A very nice, attractive but sober design.
• It must have a classy Marvaux, Quen, ... chique design.
• The logo must be on it (in attachment)
• There must be the following list in it:
• Gelaatsverzorging
• Wimperverlenging
• Wimperlifting
• Suikerontharing
• Permanente Make Up
• Airbrush Tanning
• Manicure - Pedicure - Tovira
• and then the website www.velmora.be, and the text "Enkel op afspraak, bel 0486319542"
Nice to have
• a catchy design,
• max. width can be 75 cm and max height 180 cm as it is a design for a board that will be glued on a door.
Should not have
• orchid flowers, buddha look a likes

```html
<!DOCTYPE html>
<html lang="nl">
<head>
<meta charset="utf-8">
<title>Velmora – Schoonheidsinstituut</title>
<link rel="stylesheet" href="https://fonts.googleapis.com/css2?family=Oswald:wght@300;400;500;600&family=Raleway:wght@300&display=swap">
<style>
  :root {
    --ink: #0d0d0d;
    --paper: #ffffff;
    --teal: #4f8b9b;
    --teal-edge: #3f7585;
    --text-dark: #1a1a1a;
    --wash-violet: #a99bc9;
    --wash-blue: #6f93b8;
    --wash-gold: #e8c877;
  }
  * { margin: 0; padding: 0; box-sizing: border-box; }
  html, body { width: 1200px; height: 2880px; overflow: hidden; background: var(--ink); }
  .door-board {
    position: relative;
    width: 1200px;
    height: 2880px;
    background: var(--ink);
    font-family: "Oswald", sans-serif;
    color: var(--paper);
  }
  .brand {
    position: absolute;
    left: 0; top: 0;
    width: 1200px;
    height: 820px;
    text-align: center;
  }
  .brand-name {
    position: absolute;
    left: 0; right: 0;
    top: 470px;
    font-family: "Raleway", sans-serif;
    font-weight: 300;
    font-size: 112px;
    letter-spacing: 0.32em;
    padding-left: 0.32em;
    line-height: 1;
    color: var(--paper);
  }
  .brand-tagline {
    position: absolute;
    left: 0; right: 0;
    top: 738px;
    font-family: "Raleway", sans-serif;
    font-weight: 300;
    font-size: 26px;
    letter-spacing: 0.62em;
    padding-left: 0.62em;
    line-height: 1;
    color: var(--paper);
  }
  .services {
    list-style: none;
    position: absolute;
    left: 48px;
    top: 888px;
    width: 1152px;
  }
  .service {
    height: 136px;
    margin-bottom: 28px;
    background: var(--teal);
    border-top: 4px solid var(--teal-edge);
    border-bottom: 4px solid var(--teal-edge);
    display: flex;
    align-items: center;
    padding-left: 40px;
    font-weight: 500;
    font-size: 68px;
    letter-spacing: 0.02em;
    text-transform: uppercase;
    color: var(--paper);
    white-space: nowrap;
  }
  .service:last-child { height: 144px; margin-top: 8px; }
  .bullet { margin-right: 22px; }
  .bullet-inline { margin: 0 22px; }
  .appointment {
    position: absolute;
    left: 0; top: 2128px;
    width: 1200px;
    height: 520px;
    background: var(--paper);
  }
  .eye-art {
    position: absolute;
    left: 0; top: 40px;
    width: 470px;
    height: 440px;
    background:
      radial-gradient(ellipse at 55% 45%, var(--wash-blue) 0%, rgba(111,147,184,0.5) 30%, transparent 60%),
      radial-gradient(ellipse at 25% 30%, var(--wash-violet) 0%, transparent 55%),
      radial-gradient(ellipse at 30% 85%, var(--wash-gold) 0%, transparent 50%);
  }
  .appointment-text {
    position: absolute;
    left: 578px;
    top: 142px;
    color: var(--text-dark);
    line-height: 1;
  }
  .appointment-note {
    font-weight: 300;
    font-size: 66px;
    letter-spacing: 0.04em;
    text-transform: uppercase;
  }
  .appointment-phone {
    margin-top: 48px;
    font-weight: 500;
    font-size: 66px;
    letter-spacing: 0.04em;
    text-transform: uppercase;
  }
  .website {
    position: absolute;
    left: 0; right: 0;
    top: 2648px;
    height: 232px;
    display: flex;
    align-items: center;
    justify-content: center;
    font-weight: 600;
    font-size: 70px;
    letter-spacing: 0.3em;
    padding-left: 0.3em;
    text-transform: uppercase;
    color: var(--paper);
  }
</style>
</head>
<body>
  <main class="door-board">
    <header class="brand">
      <div class="brand-name">VELMORA</div>
      <div class="brand-tagline">SCHOONHEIDSINSTITUUT</div>
    </header>

    <ul class="services">
      <li class="service"><span class="bullet">•</span>Gelaatsverzorging</li>
      <li class="service"><span class="bullet">•</span>Wimperverlenging</li>
      <li class="service"><span class="bullet">•</span>Wimperlifting</li>
      <li class="service"><span class="bullet">•</span>Suikerontharing</li>
      <li class="service"><span class="bullet">•</span>Permanente Make Up</li>
      <li class="service"><span class="bullet">•</span>Airbrush Tanning</li>
      <li class="service"><span class="bullet">•</span>Manicure<span class="bullet-inline">•</span>Pedicure<span class="bullet-inline">•</span>Tovira</li>
    </ul>

    <section class="appointment">
      <div class="eye-art" role="img" aria-label="Watercolour illustration of a made-up eye"></div>
      <div class="appointment-text">
        <p class="appointment-note">Enkel op afspraak</p>
        <p class="appointment-phone">Bel 0486319542</p>
      </div>
    </section>

    <footer class="website">www.velmora.be</footer>
  </main>
</body>
</html>
```